One Pager Website for various security awareness videos

We need a one pager website (design & coding) for our security awareness video series. We imagine placing a few (3-4 sample videos) on the website, a customer referal and some contact form. SOmething similar to https://brevko.com/watch-now/. Here are some of the videos which we will place on the website:
https://www.clipvane.com/watch?v=Qa7pLm2Xw9T&t=112s
https://www.clipvane.com/watch?v=Hr4ZkeN8bVd
https://www.clipvane.com/watch?v=_9wjTPLC3KA
https://www.clipvane.com/watch?v=bvRQQsGtuHx
https://www.clipvane.com/watch?v=4yd81NkDa3p
https://www.clipvane.com/watch?v=eTWo2JsUkqC
https://www.clipvane.com/watch?v=VzPRGhd5sYo
https://www.clipvane.com/watch?v=73GkF6tWxxN
https://www.clipvane.com/watch?v=58jfZeqnK1R
As for logo: our company www.maravelguard.com is the creator of those videos. You can use our logo / name.
B2B security officers in large enterprises
1 page

```html
<!DOCTYPE html>
<html lang="en">
<head>
<meta charset="utf-8">
<title>Vesta – Watch the Season Lineup</title>
<link rel="stylesheet" href="https://fonts.googleapis.com/css2?family=Poppins:wght@400;500;600;700;800&display=swap">
<style>
:root{
  --teal:#15b9c5;
  --teal-dark:#0fa9b5;
  --orange:#f7941d;
  --orange-deep:#ff7a00;
  --ink:#111111;
  --body:#444444;
  --muted:#666666;
  --grey-bg:#f1f1f1;
  --field:#e9e9e9;
  --white:#ffffff;
}
*{box-sizing:border-box;margin:0;padding:0}
html,body{width:1200px;height:3658px;overflow:hidden;background:var(--white)}
body{font-family:'Poppins',sans-serif;color:var(--ink)}
.page{position:relative;width:1200px;height:3658px;overflow:hidden}
.abs{position:absolute}
.btn{position:absolute;display:flex;align-items:center;justify-content:center;border-radius:20px;font-weight:700;font-size:13px;text-transform:uppercase;letter-spacing:.2px}
.btn-solid{background:var(--orange);color:var(--white)}
.btn-outline{border:2px solid var(--orange);color:var(--ink);background:var(--white)}

/* header */
.brand{position:absolute;display:flex;align-items:center;gap:8px;font-weight:800;font-size:28px;color:var(--ink)}
.brand-dot{width:30px;height:30px;border-radius:50%;background:var(--orange)}
.nav{position:absolute;top:30px;right:88px;display:flex;gap:30px}
.nav a{color:var(--white);font-size:12.5px;font-weight:600;text-decoration:none;text-transform:uppercase}
.nav a:first-child{text-transform:none}

/* hero */
.hero-kicker{left:88px;top:260px;color:var(--white);font-size:29px;font-weight:400}
.hero-title{left:88px;top:290px;color:var(--white);font-size:60px;font-weight:800;line-height:1;letter-spacing:.5px}
.hero-sub{left:88px;top:356px;color:var(--white);font-size:16px;line-height:23px;width:300px}
.hero-card{left:585px;top:206px;width:525px;height:332px;background:var(--white);border-radius:14px;box-shadow:0 20px 40px rgba(0,0,0,.12);padding:24px}
.art{width:100%;height:100%;border-radius:6px}
.play{position:absolute;left:50%;top:50%;width:72px;height:72px;margin:-48px 0 0 -12px;border-radius:50%;background:var(--orange);display:flex;align-items:center;justify-content:center}

/* latest episode */
.section-title{position:absolute;left:0;width:1200px;text-align:center;font-size:35px;font-weight:700;line-height:36px;text-transform:uppercase}
.episode-card{left:114px;top:933px;width:460px;height:274px;background:var(--white);border-radius:14px;box-shadow:0 18px 40px rgba(0,0,0,.12);padding:0}
.ep-kicker{left:632px;top:972px;color:var(--orange);font-size:23px;font-weight:400}
.ep-title{left:632px;top:1000px;font-size:24px;font-weight:700}
.ep-text{left:632px;top:1032px;width:430px;font-size:14px;line-height:22.5px;color:var(--body)}

/* seasons */
.tabs{position:absolute;top:1512px;left:0;width:1200px;display:flex;justify-content:center;gap:46px}
.tab{text-align:center;padding-bottom:10px;width:136px}
.tab .year{color:var(--teal);font-size:19px;font-weight:600;line-height:22px}
.tab .name{font-size:23px;font-weight:700;line-height:28px}
.tab.active .year{color:var(--orange-deep)}
.tab.active{border-bottom:3px solid var(--orange-deep)}
.video-card{position:absolute;top:1612px;width:247px;height:228px;background:var(--white);border-radius:10px;box-shadow:0 4px 14px rgba(0,0,0,.06);padding:22px}
.video-title{position:absolute;top:1857px;font-size:19px;font-weight:600;width:250px}
.video-sub{position:absolute;top:1885px;font-size:14px;color:var(--muted)}

/* testimonial */
.quote{left:88px;top:2180px;width:540px;font-size:24px;line-height:34px;font-weight:400}
.quote-by{left:88px;top:2323px;font-size:14px;color:var(--muted)}
.divider{left:88px;top:2530px;width:1022px;height:1px;background:#e3e3e3}

/* form */
.form-title{left:132px;top:2650px;font-size:36px;font-weight:700}
.field{position:absolute;height:40px;background:var(--field);border-radius:3px;font-size:13px;color:#888;padding:0 17px;display:flex;align-items:center}
.label{position:absolute;font-size:13px;font-weight:600}
.note{position:absolute;font-size:12.5px;color:var(--body)}
.check{position:absolute;display:flex;align-items:center;gap:6px;font-size:12.5px;color:var(--body)}
.check span{width:11px;height:11px;border:1.5px solid #333;border-radius:2px}

/* contact */
.contact-title{left:694px;top:2650px;font-size:36px;font-weight:700}
.info{position:absolute;left:694px;display:flex;gap:16px}
.info-icon{width:32px;height:32px;border-radius:50%;background:var(--teal);display:flex;align-items:center;justify-content:center;flex-shrink:0}
.info h4{font-size:14px;font-weight:700;text-transform:uppercase;line-height:18px}
.info p{font-size:16px;line-height:21px;color:#333}

/* footer */
.foot-col{position:absolute;top:3372px}
.foot-col h5{color:var(--white);font-size:15px;font-weight:700;text-transform:uppercase;margin-bottom:14px}
.foot-col a{display:block;color:var(--white);font-size:12.5px;text-transform:uppercase;text-decoration:none;line-height:27px}
.foot-line{left:88px;top:3607px;width:1022px;height:1px;background:rgba(255,255,255,.35)}
.copyright{left:88px;top:3621px;color:var(--white);font-size:15px}
.social{position:absolute;top:3624px;display:flex;gap:22px;left:978px}
.social span{width:16px;height:16px;border-radius:50%;background:var(--white)}
.to-top{left:1132px;top:3576px;width:34px;height:34px;border-radius:50%;background:var(--orange-deep);display:flex;align-items:center;justify-content:center}
</style>
</head>
<body>
<div class="page">

  <!-- hero background -->
  <svg class="abs" style="left:0;top:0" width="1200" height="720" aria-hidden="true">
    <path d="M0,0 H1200 V440 C1120,420 1000,440 900,530 C800,625 720,700 600,696 C470,692 420,628 300,628 C170,628 80,650 0,660 Z" fill="var(--teal)"/>
  </svg>
  <div class="abs" role="img" aria-label="Faint line drawing of an office worker at a desk by a window" style="left:0;top:60px;width:560px;height:520px;background:radial-gradient(ellipse at 40% 50%,rgba(255,255,255,.08),rgba(255,255,255,0) 70%)"></div>

  <header>
    <div class="brand" style="left:88px;top:20px"><span class="brand-dot"></span>Vesta</div>
    <nav class="nav">
      <a href="#">Corvell Insights</a>
      <a href="#">Solutions</a>
      <a href="#">Delivery</a>
      <a href="#">Resources</a>
      <a href="#">Get Pricing</a>
    </nav>
  </header>

  <section class="hero">
    <div class="abs hero-kicker">SEASON LINEUP</div>
    <h1 class="abs hero-title">WATCH VESTA</h1>
    <p class="abs hero-sub">Cyber Security Awareness: Malware &amp; Spear Phishing</p>
    <a class="btn btn-solid" style="left:88px;top:412px;width:159px;height:32px">Watch Episodes</a>
    <div class="abs hero-card">
      <div class="art" role="img" aria-label="Cartoon monitor showing a ransomware warning screen" style="background:linear-gradient(135deg,#1b1b1b 0%,#1b1b1b 18%,#d62e2e 18%,#c92626 55%,#f4f4f4 55%)"></div>
      <div class="play"><svg width="26" height="28" viewBox="0 0 26 28"><path d="M3,2 L24,14 L3,26 Z" fill="#fff"/></svg></div>
    </div>
  </section>

  <!-- latest episode -->
  <svg class="abs" style="left:0;top:838px" width="460" height="430" aria-hidden="true">
    <defs><linearGradient id="blob" x1="0" y1="0" x2="1" y2="1"><stop offset="0" stop-color="#ff9a1f"/><stop offset="1" stop-color="#ff7a00"/></linearGradient></defs>
    <path d="M0,60 C120,0 300,-20 420,60 C470,100 420,200 330,260 C270,300 250,420 170,428 C100,435 40,380 0,360 Z" fill="url(#blob)"/>
  </svg>
  <h2 class="section-title" style="top:795px">One of our<br>latest episodes</h2>
  <div class="abs episode-card">
    <div class="art" role="img" aria-label="Line drawing of an office worker reading a document beside a desk" style="border-radius:14px;background:linear-gradient(180deg,#fafafa,#ececec)"></div>
  </div>
  <div class="abs ep-kicker">SEASON 6 | EPISODE 4</div>
  <h3 class="abs ep-title">DON'T FALL FOR IT</h3>
  <p class="abs ep-text">Lorem Ipsum is simply dummy text of the printing and typesetting industry. Lorem Ipsum has been the industry's standard dummy text ever since the 1500s, when an unknown printer took a galley of type and scrambled it to make ...</p>
  <a class="btn btn-outline" style="left:632px;top:1136px;width:132px;height:32px">Get Pricing</a>

  <!-- seasons -->
  <svg class="abs" style="left:0;top:1250px" width="1200" height="785" aria-hidden="true">
    <path d="M0,175 C120,215 300,80 560,25 C780,-15 1000,0 1200,40 V785 H0 Z" fill="var(--grey-bg)"/>
  </svg>
  <div class="tabs">
    <div class="tab active"><div class="year">2021</div><div class="name">SEASON 6</div></div>
    <div class="tab"><div class="year">2020</div><div class="name">SEASON 5</div></div>
    <div class="tab"><div class="year">2019</div><div class="name">SEASON 4</div></div>
    <div class="tab"><div class="year">2018</div><div class="name">SEASON 3</div></div>
  </div>

  <div class="video-card" style="left:88px"><div class="art" role="img" aria-label="Line drawing of a worker at a computer desk" style="background:linear-gradient(180deg,#fbfbfb,#eeeeee)"></div></div>
  <div class="video-card" style="left:348px"><div class="art" role="img" aria-label="Cartoon monitor showing a change password dialog" style="background:linear-gradient(180deg,#fff 20%,#1f6bb8 20%,#1f6bb8 80%,#fff 80%)"></div></div>
  <div class="video-card" style="left:606px"><div class="art" role="img" aria-label="Cartoon monitor showing a user login screen" style="background:linear-gradient(180deg,#fff 20%,#173a6b 20%,#173a6b 80%,#fff 80%)"></div></div>
  <div class="video-card" style="left:865px"><div class="art" role="img" aria-label="Line drawing of a presenter beside a flip chart about passwords" style="background:linear-gradient(180deg,#fbfbfb,#eeeeee)"></div></div>

  <div class="video-title" style="left:88px">Cyber Security Aware..</div>
  <div class="video-sub" style="left:88px">Malware &amp; Spear Phishing</div>
  <div class="video-title" style="left:350px">VESTA | Marty learns</div>
  <div class="video-sub" style="left:350px">About Password Security</div>
  <div class="video-title" style="left:605px">Cyber Security Aware..</div>
  <div class="video-sub" style="left:605px">Malware &amp; Spear Phishing</div>
  <div class="video-title" style="left:866px">VESTA | Marty learns</div>
  <div class="video-sub" style="left:866px">About Password Security</div>

  <!-- testimonial -->
  <blockquote class="abs quote">The cybersecurity videos are fast, fun, and easy to distribute to employees. We've seen click-through rates on spam test emails drop rapidly.</blockquote>
  <div class="abs quote-by">— Accounting Director in Government | 50M – 250M USD</div>
  <svg class="abs" style="left:740px;top:2128px" width="380" height="326" aria-hidden="true">
    <path d="M280,10 C340,-20 370,60 340,160 C310,260 200,330 90,318 C30,312 10,280 40,270 C150,240 200,60 280,10 Z" fill="var(--teal)"/>
  </svg>
  <div class="abs" role="img" aria-label="Laptop showing a phishing and malware simulation animation" style="left:700px;top:2160px;width:420px;height:250px;border-radius:10px 10px 4px 4px;background:linear-gradient(180deg,#2b2b2b 0 8px,#f4f4f4 8px 92%,#9a9a9a 92%)"></div>
  <div class="abs" role="img" aria-label="Cartoon monkey mascot sitting beside the laptop" style="left:610px;top:2296px;width:125px;height:130px;border-radius:50%;background:radial-gradient(circle at 50% 45%,#ffb42a,#f39200)"></div>
  <div class="abs divider"></div>

  <!-- form -->
  <h2 class="abs form-title">SPEAK WITH AN EXPERT</h2>
  <form>
    <div class="field" style="left:132px;top:2712px;width:239px">First name*</div>
    <div class="field" style="left:379px;top:2712px;width:239px">Last name*</div>
    <div class="field" style="left:132px;top:2762px;width:239px">Business email*</div>
    <div class="field" style="left:379px;top:2762px;width:239px">Company name*</div>
    <div class="field" style="left:132px;top:2812px;width:239px">Company size*</div>
    <div class="field" style="left:379px;top:2812px;width:239px">How did you hear about Vesta*</div>
    <div class="label" style="left:132px;top:2868px">Best contact number to reach you*</div>
    <div class="field" style="left:132px;top:2892px;width:486px">Best phone number to reach you</div>
    <div class="note" style="left:132px;top:2954px">Provide an accurate user count to ensure the correct VESTA representative is assigned.</div>
    <div class="check" style="left:132px;top:2984px"><span></span>Click here if you'd like pricing information</div>
    <div class="check" style="left:132px;top:3004px"><span></span>I am interested in reselling VESTA</div>
    <a class="btn btn-solid" style="left:132px;top:3046px;width:135px;height:38px">Get Pricing</a>
  </form>

  <!-- contact -->
  <h2 class="abs contact-title">CONTACT INFO</h2>
  <div class="info" style="top:2716px">
    <div class="info-icon"><svg width="14" height="16" viewBox="0 0 14 16"><path d="M7,0 C3,0 1,3 1,6 C1,10 7,16 7,16 C7,16 13,10 13,6 C13,3 11,0 7,0 Z" fill="#fff"/><circle cx="7" cy="6" r="2.2" fill="var(--teal)"/></svg></div>
    <div><h4>Location</h4><p>Some address line goes here city name<br>country name goes here</p></div>
  </div>
  <div class="info" style="top:2802px">
    <div class="info-icon"><svg width="14" height="14" viewBox="0 0 14 14"><path d="M3,1 L5,1 L6,4 L4.5,5.5 C5.5,7.5 6.5,8.5 8.5,9.5 L10,8 L13,9 L13,11 C13,12 12,13 11,13 C5.5,12.5 1.5,8.5 1,3 C1,2 2,1 3,1 Z" fill="#fff"/></svg></div>
    <div><h4>Phone</h4><p>800-555-0147</p></div>
  </div>
  <div class="info" style="top:2860px">
    <div class="info-icon"><svg width="14" height="12" viewBox="0 0 14 12"><rect x="0.5" y="1" width="13" height="10" rx="1" fill="#fff"/><path d="M1,2 L7,7 L13,2" stroke="var(--teal)" stroke-width="1.4" fill="none"/></svg></div>
    <div><h4>Email</h4><p>hello@vesta-aware.example</p></div>
  </div>
  <div class="info" style="top:2926px">
    <div class="info-icon"><svg width="14" height="14" viewBox="0 0 14 14"><circle cx="7" cy="7" r="6" fill="#fff"/><path d="M7,3.5 V7 L9.5,8.5" stroke="var(--teal)" stroke-width="1.5" fill="none"/></svg></div>
    <div><h4>Opening Hours</h4><p>MONDAY - SUNDAY: 8:30 AM - 6:00 PM</p></div>
  </div>

  <!-- footer -->
  <svg class="abs" style="left:0;top:3000px" width="1200" height="658" aria-hidden="true">
    <defs><linearGradient id="edge" x1="0" y1="0" x2="1" y2="0"><stop offset="0" stop-color="var(--orange)"/><stop offset=".55" stop-color="var(--orange)"/><stop offset=".75" stop-color="var(--orange)" stop-opacity="0"/></linearGradient></defs>
    <path d="M0,180 C120,225 250,252 420,244 C650,232 820,60 1200,6" stroke="url(#edge)" stroke-width="14" fill="none"/>
    <path d="M0,196 C120,238 250,262 420,254 C650,242 820,70 1200,12 V658 H0 Z" fill="var(--teal)"/>
  </svg>
  <div class="brand" style="left:114px;top:3428px;font-size:40px"><span class="brand-dot" style="width:44px;height:44px"></span>Vesta</div>

  <div class="foot-col" style="left:378px"><h5>Navigate</h5><a href="#">About</a><a href="#">Partnerships</a><a href="#">Blog</a><a href="#">Contact</a><a href="#">Free Trial</a></div>
  <div class="foot-col" style="left:532px"><h5>Solutions</h5><a href="#">Vesta Aware Anime</a><a href="#">Vesta Aware Corporate</a><a href="#">Vesta Aware Enterprise</a></div>
  <div class="foot-col" style="left:751px"><h5>Compliance</h5><a href="#">Vesta PCI</a><a href="#">Vesta HIPAA</a><a href="#">Vesta GDPR</a><a href="#">Vesta CCPA</a></div>
  <div class="foot-col" style="left:923px"><h5>Community</h5><a href="#">Vesta Family</a><a href="#">Vesta K-12 + University</a><a href="#">Vesta Security for Good</a></div>

  <div class="abs foot-line"></div>
  <div class="abs copyright">©Copyright 2021 | All Rights Reserved</div>
  <div class="social" aria-label="Social links"><span></span><span></span><span></span><span></span></div>
  <div class="abs to-top"><svg width="12" height="14" viewBox="0 0 12 14"><path d="M6,13 V2 M2,6 L6,2 L10,6" stroke="#fff" stroke-width="1.6" fill="none"/></svg></div>

</div>
</body>
</html>
```